Business Card - TUMDE

We need business cards for our dog rescue... we have a wonderful logo which I am including. The front of the card should show our contact information and our logo. The back should show our two dog adoption site addresses:

www.Woflinto.com/shelter40519-pets.html
www.houndlocket.com/shelters/tn519.html

```html
<!DOCTYPE html>
<html lang="en">
<head>
<meta charset="utf-8">
<title>TUMDE Business Card</title>
<link rel="stylesheet" href="https://fonts.googleapis.com/css2?family=Open+Sans:wght@300;600&family=Courgette&display=swap">
<style>
  :root {
    --page-bg: #e9ecef;
    --sky-light: #7cc3f1;
    --sky-mid: #4aa6e6;
    --sky-deep: #2f8bd3;
    --navy: #111a2c;
    --navy-soft: #27324a;
    --fur-tan: #b8864e;
    --cage-grey: #8b9099;
    --band-blue: #3a8fd8;
    --ink-white: #ffffff;
    --logo-red: #d8232a;
    --script-tint: #eaf6ff;
  }
  * { box-sizing: border-box; margin: 0; padding: 0; }
  html, body { width: 1200px; height: 900px; overflow: hidden; }
  body {
    background: var(--page-bg);
    font-family: "Open Sans", sans-serif;
    position: relative;
  }
  .card {
    position: absolute;
    left: 250px;
    width: 700px;
    height: 400px;
    overflow: hidden;
    box-shadow: 0 6px 18px rgba(0,0,0,0.18);
  }
  .card--back { top: 35px; background: linear-gradient(135deg, var(--sky-light), var(--sky-mid) 55%, var(--sky-deep)); }
  .card--front { top: 465px; background: var(--navy); }

  /* brand mark */
  .brand { display: flex; align-items: center; gap: 10px; }
  .brand__dot { width: 26px; height: 26px; border-radius: 50%; background: var(--logo-red); }
  .brand__name { font-weight: 600; font-size: 26px; color: var(--ink-white); letter-spacing: 1px; }

  /* back side */
  .card--back .brand { position: absolute; left: 50px; top: 130px; }
  .faint-disc {
    position: absolute; left: 150px; top: 60px; width: 200px; height: 200px;
    border-radius: 50%; background: rgba(255,255,255,0.12);
  }
  .websites { position: absolute; right: 40px; top: 105px; text-align: right; }
  .websites__title {
    font-family: "Courgette", cursive; font-size: 30px; color: var(--script-tint);
    margin-bottom: 18px;
  }
  .websites__url { font-weight: 300; font-size: 21px; color: var(--ink-white); line-height: 1.7; }

  /* front side */
  .photo {
    position: absolute; inset: 0;
    background:
      linear-gradient(120deg, var(--navy) 0%, var(--navy-soft) 38%, transparent 55%),
      radial-gradient(ellipse at 70% 65%, var(--fur-tan) 0%, #8a6038 30%, var(--cage-grey) 60%, #3b4150 100%);
  }
  .card--front .brand { position: absolute; left: 270px; top: 26px; }
  .contact {
    position: absolute; left: 40px; top: 120px; list-style: none;
    color: var(--ink-white); font-weight: 300; font-size: 20px; line-height: 1.75;
  }
  .band {
    position: absolute; left: 0; right: 0; bottom: 0; height: 34px;
    background: var(--band-blue); border-top: 4px solid var(--ink-white);
  }
</style>
</head>
<body>
  <section class="card card--back" aria-label="Card back">
    <div class="faint-disc"></div>
    <div class="brand">
      <span class="brand__dot"></span>
      <span class="brand__name">TUMDE</span>
    </div>
    <div class="websites">
      <p class="websites__title">Visit us at our websites</p>
      <p class="websites__url">www.Woflinto.com/shelter40519-pets.html</p>
      <p class="websites__url">www.houndlocket.com/shelters/tn519.html</p>
    </div>
  </section>

  <section class="card card--front" aria-label="Card front">
    <div class="photo" role="img" aria-label="Photo of a tan rescue puppy resting behind the wire bars of a kennel"></div>
    <div class="brand">
      <span class="brand__dot"></span>
      <span class="brand__name">TUMDE</span>
    </div>
    <ul class="contact">
      <li>Your Address Here</li>
      <li>Telephone No. 123-456</li>
      <li>Email: youremailhere@tumdemail.org</li>
    </ul>
    <div class="band"></div>
  </section>
</body>
</html>
```